Flyer for Cool Choir Concert

8.5x11 color flyer, to get people to attend excellent concert

Requirements
Should not have
• I don't like a lot of musical symbols incorporated into the design.

```html
<!DOCTYPE html>
<html lang="en">
<head>
<meta charset="utf-8">
<title>War &amp; Peace – Concert Flyer</title>
<link rel="stylesheet" href="https://fonts.googleapis.com/css2?family=Cinzel:wght@400;700;900&family=Open+Sans:wght@400;600;700;800&family=Pinyon+Script&display=swap">
<style>
  :root {
    --purple: #4a2670;
    --purple-deep: #3b1f5e;
    --blue: #1aa0dc;
    --blue-dark: #0b77b0;
    --crimson: #b5124f;
    --crimson-deep: #8e0d3d;
    --cream: #f5e6b8;
    --paper: #f4f5f7;
    --paper-edge: #dfe2e6;
    --ink: #222;
    --stage: #ececec;
  }
  * { box-sizing: border-box; margin: 0; padding: 0; }
  html, body { width: 1200px; height: 1200px; overflow: hidden; background: var(--stage); }
  .flyer {
    position: absolute; left: 175px; top: 50px; width: 850px; height: 1100px;
    background: linear-gradient(180deg, #ffffff 0%, var(--paper) 45%, var(--paper-edge) 70%, #ffffff 100%);
    font-family: "Open Sans", Arial, sans-serif; overflow: hidden;
  }
  .flyer > * { position: absolute; }

  .brand-name {
    top: 26px; left: 0; width: 100%; text-align: center;
    font-family: "Cinzel", Georgia, serif; font-weight: 400; font-size: 50px;
    color: var(--purple); letter-spacing: 1px;
  }

  .directors-band { left: 0; top: 128px; width: 850px; height: 62px; }
  .directors {
    top: 138px; left: 0; width: 100%; text-align: center;
    color: var(--cream); font-weight: 600; font-size: 17.5px;
  }

  .presents {
    top: 182px; left: 0; width: 100%; text-align: center;
    font-weight: 700; font-size: 15px; letter-spacing: 7px; color: var(--purple-deep);
  }

  .title { font-family: "Cinzel", Georgia, serif; font-weight: 700; line-height: 1; }
  .title-war {
    top: 214px; left: 208px; font-size: 128px; color: var(--blue);
    text-shadow: 3px 3px 0 rgba(0,60,110,.35);
  }
  .title-amp {
    top: 268px; left: 518px; font-size: 60px; line-height: 1; color: var(--blue);
    font-family: "Cinzel", Georgia, serif; font-weight: 700;
  }
  .title-peace {
    top: 330px; left: 190px; font-size: 132px; color: var(--crimson);
    text-shadow: 3px 3px 0 rgba(80,90,120,.35);
  }

  .flourish {
    background: linear-gradient(90deg, rgba(26,160,220,.18), rgba(181,18,79,.18));
    border-radius: 50%;
  }
  .flourish-left { left: 48px; top: 262px; width: 155px; height: 120px; }
  .flourish-right { left: 650px; top: 262px; width: 155px; height: 120px; }
  .flourish-bottom-left { left: 12px; top: 985px; width: 160px; height: 80px; background: rgba(181,18,79,.15); }
  .flourish-bottom-right { left: 690px; top: 985px; width: 160px; height: 80px; background: rgba(181,18,79,.15); }

  .choir-photo {
    left: 28px; top: 462px; width: 600px; height: 340px;
    border-radius: 60px 50px 20px 20px;
    background: radial-gradient(ellipse at 50% 45%, #6b6163 0%, #2c2a2c 55%, #1a1a1b 100%);
  }

  .dates { right: 25px; top: 482px; text-align: right; }
  .date-day { color: var(--crimson); font-weight: 800; font-size: 24px; line-height: 1.1; }
  .date-line { color: var(--purple); font-weight: 700; font-size: 27px; line-height: 1.1; }
  .date-block + .date-block { margin-top: 14px; }

  .venue {
    right: 25px; top: 708px; text-align: right;
    color: var(--purple-deep); font-weight: 700; font-size: 16.5px; line-height: 1.22;
  }

  .ribbons { left: 0; top: 760px; width: 850px; height: 240px; }

  .ribbon-text { color: #fff; text-align: center; font-weight: 700; }
  .join {
    left: 20px; top: 806px; width: 420px; transform: rotate(-4.5deg);
    font-size: 17px; line-height: 1.3;
  }
  .script { font-family: "Pinyon Script", cursive; font-weight: 400; font-size: 34px; line-height: 1.1; color: var(--cream); display: block; }
  .featuring {
    left: 445px; top: 808px; width: 400px; transform: rotate(5deg);
    font-size: 17px; line-height: 1.3;
  }
  .featuring .script { font-size: 42px; }

  .tickets { top: 956px; left: 0; width: 100%; text-align: center; }
  .tickets-head { color: var(--crimson); font-weight: 800; font-size: 23px; }
  .tickets-prices { color: var(--purple); font-weight: 700; font-size: 18px; margin-top: 2px; }
  .tickets-note { color: var(--ink); font-size: 15px; margin-top: 8px; }
  .website {
    top: 1052px; left: 0; width: 100%; text-align: center;
    color: var(--purple); font-weight: 700; font-size: 20px;
  }
</style>
</head>
<body>
<main class="flyer">
  <div class="brand-name">LUMINARA</div>

  <svg class="directors-band" viewBox="0 0 850 62" aria-hidden="true">
    <defs>
      <linearGradient id="bandGrad" x1="0" x2="1">
        <stop offset="0" stop-color="#4a2670"/><stop offset="1" stop-color="#1aa0dc"/>
      </linearGradient>
    </defs>
    <polygon points="0,34 88,34 88,58 0,52" fill="#0b77b0"/>
    <polygon points="762,34 850,34 850,52 762,58" fill="#0b77b0"/>
    <rect x="23" y="2" width="804" height="42" fill="url(#bandGrad)"/>
  </svg>
  <div class="directors">Daniel Harlow, Artistic Director | Rosa Menendez Clark, Executive Director</div>

  <div class="presents">PRESENTS</div>

  <div class="flourish flourish-left" role="img" aria-label="Decorative flourish"></div>
  <div class="flourish flourish-right" role="img" aria-label="Decorative flourish"></div>

  <div class="title title-war">WAR</div>
  <div class="title-amp">&amp;</div>
  <div class="title title-peace">PEACE</div>

  <div class="choir-photo" role="img" aria-label="Group photo of the choir singers in black gathered around a grand piano"></div>

  <div class="dates">
    <div class="date-block">
      <div class="date-day">SATURDAY</div>
      <div class="date-line">October 13</div>
      <div class="date-line">at 7:30pm</div>
    </div>
    <div class="date-block">
      <div class="date-day">SUNDAY</div>
      <div class="date-line">October 14</div>
      <div class="date-line">at 3:00pm</div>
    </div>
  </div>

  <div class="venue">St. Brendan's<br>Community Church<br>1480 Mesa Vista Road<br>NE Albuquerque</div>

  <svg class="ribbons" viewBox="0 0 850 240" aria-hidden="true">
    <defs>
      <linearGradient id="joinGrad" x1="0" x2="1">
        <stop offset="0" stop-color="#4a2670"/><stop offset="1" stop-color="#1aa0dc"/>
      </linearGradient>
      <linearGradient id="featGrad" x1="0" x2="1">
        <stop offset="0" stop-color="#d0145a"/><stop offset="1" stop-color="#8e0d3d"/>
      </linearGradient>
    </defs>
    <polygon points="0,168 88,162 88,198 0,186" fill="#0b77b0"/>
    <polygon points="0,52 442,10 444,130 0,172" fill="url(#joinGrad)"/>
    <polygon points="770,180 850,184 850,222 770,196" fill="#8e0d3d"/>
    <polygon points="436,30 850,52 850,186 434,162" fill="url(#featGrad)"/>
  </svg>

  <div class="ribbon-text join">
    <span class="script">Join the Singers of Luminara</span>
    as we perform music borne out of warfare<br>and conflict, and music that celebrates<br>peace and love
  </div>
  <div class="ribbon-text featuring">
    <span class="script">Featuring</span>
    music of Mark Ellison, Joan Sheridan,<br>Wes Tolland, Alma Parrish,<br>and others
  </div>

  <div class="flourish flourish-bottom-left" role="img" aria-label="Decorative flourish"></div>
  <div class="flourish flourish-bottom-right" role="img" aria-label="Decorative flourish"></div>

  <div class="tickets">
    <div class="tickets-head">TICKETS AVAILABLE ONLINE &amp; AT THE DOOR</div>
    <div class="tickets-prices">General $20 | Seniors $15 | Students $10</div>
    <div class="tickets-note">Complimentary childcare provided at both performances.</div>
  </div>

  <div class="website">www.luminara-choir.com</div>
</main>
</body>
</html>
```